Larkfield Prose Studio (LPStudio.net)

We need a Wordpress-based site designed for a client who provides writing and editing services for the IT industry. We have a wireframe complete for the homepage, but need all internal pages designed (based on homepage wireframe) and the entire site coded for WP.

Internal pages include: "Our Work" (with samples & testimonials); "Capabilities" (with sections to address "strategy", "coaching", "writing" and "editing"); "About Us"; and a Contact page.

Will provide all copywriting, writing samples, testimonials, and client logos.

We completely realize/acknowledge the subject matter is visually BORING! Anything at all that can be done to make it look visually appealing would be *great*! Stock photography is fine.

Please feel free to ask any questions whatsoever. Thanks for your time!

```html
<!DOCTYPE html>
<html lang="en">
<head>
<meta charset="utf-8">
<title>Larkfield Prose Studio – Internal Pages</title>
<link href="https://fonts.googleapis.com/css2?family=Oswald:wght@500;600&family=Roboto:ital,wght@0,400;0,500;0,700;1,400&display=swap" rel="stylesheet">
<style>
:root{
  --blue:#1f62a8;
  --footer-text:#86addb;
  --ink:#1c1c1c;
  --body:#3b3b3b;
  --canvas:#e5e5e5;
  --white:#ffffff;
  --tint:#eef3f9;
  --card:#f3f6fa;
  --line:#e3e6ea;
  --label:#7a7a7a;
  --star:#f2a91b;
}
*{box-sizing:border-box;margin:0;padding:0}
html,body{width:1200px;height:2496px;overflow:hidden}
body{background:var(--canvas);font-family:'Roboto',sans-serif;color:var(--body);position:relative}
.page-label{position:absolute;font-weight:500;font-size:24px;color:#7b7b7b;transform:translateX(-50%);white-space:nowrap}
.panel{position:absolute;width:431px;background:var(--white);overflow:hidden}
.panel > *{position:absolute}
/* header */
.site-header{left:0;top:0;width:431px;height:36px;background:var(--white)}
.site-header .wordmark{position:absolute;left:13px;top:12px;font-family:'Oswald',sans-serif;font-weight:600;font-size:10px;color:var(--blue);white-space:nowrap}
.site-nav{position:absolute;left:154px;top:0;height:36px;display:flex;gap:13px;align-items:center}
.site-nav a{font-family:'Oswald',sans-serif;font-weight:500;font-size:6px;color:#222;height:36px;line-height:36px;position:relative;letter-spacing:.2px}
.site-nav a.active{color:var(--blue)}
.site-nav a.active::after{content:"";position:absolute;left:0;right:0;bottom:0;height:2px;background:var(--blue)}
.btn-touch{position:absolute;left:360px;top:11px;width:58px;height:16px;border-radius:8px;background:var(--blue);color:var(--white);font-family:'Oswald',sans-serif;font-weight:500;font-size:6px;line-height:16px;text-align:center}
/* hero */
.hero{left:0;top:36px;width:431px;height:163px}
.hero-photo{position:absolute;inset:0;background:linear-gradient(100deg,#f4f6f8 0%,#e9edf1 24%,#c9ccd0 33%,#4d5157 41%,#3a3d42 49%,#e7e3e3 55%,#cfc9c8 60%,#5a5e64 66%,#474b51 74%,#9aa1a8 82%,#e6e9ec 89%,#d5d9dd 93%,#24272b 97%)}
.hero-title{position:absolute;left:38px;top:44px;font-family:'Oswald',sans-serif;font-weight:600;font-size:21px;line-height:25px;color:var(--ink);text-transform:uppercase}
/* common */
.section-title{left:0;width:431px;text-align:center;font-family:'Oswald',sans-serif;font-weight:600;font-size:20px;color:var(--blue);text-transform:uppercase;line-height:26px}
.section-intro{left:50%;transform:translateX(-50%);text-align:center;font-size:7px;line-height:10px;color:#222}
.site-footer{left:0;width:431px;background:var(--blue);display:flex;align-items:center;justify-content:center;font-weight:500;font-size:23px;color:var(--footer-text)}
/* our work */
.btn-pill{background:var(--blue);color:var(--white);font-family:'Oswald',sans-serif;font-weight:500;font-size:6px;text-align:center;border-radius:10px}
.divider{left:0;width:431px;height:1px;background:var(--line)}
.testimonial{width:107px;height:166px;background:var(--card)}
.testimonial .quote-mark{position:absolute;left:13px;top:6px;font-family:'Oswald',sans-serif;font-weight:600;font-size:40px;line-height:40px;color:var(--blue)}
.testimonial p{position:absolute;left:15px;top:38px;width:80px;font-style:italic;font-size:6px;line-height:8.6px;color:var(--blue)}
.testimonial .avatar{position:absolute;left:14px;top:132px;width:26px;height:26px;border-radius:50%;background:radial-gradient(circle at 50% 40%,#e2c9b4 0%,#b59a86 40%,#d7dbe0 75%)}
.testimonial .name{position:absolute;left:47px;top:136px;font-size:6px;font-weight:700;color:var(--blue)}
.testimonial .stars{position:absolute;left:47px;top:144px;font-size:6px;color:var(--star);letter-spacing:.5px}
.dots{left:0;width:431px;text-align:center;font-size:10px;color:var(--blue);letter-spacing:1px;font-weight:700}
/* capabilities */
.cap-image{width:145px;height:157px}
.cap-image.skew-left{clip-path:polygon(0 8%,100% 0,100% 100%,0 94%)}
.cap-image.skew-right{clip-path:polygon(0 0,100% 12%,100% 92%,0 100%)}
.cap-icon{width:44px;height:44px;border-radius:50%;background:var(--white);box-shadow:0 1px 6px rgba(0,0,0,.15);display:flex;align-items:center;justify-content:center}
.cap-title{font-family:'Oswald',sans-serif;font-weight:600;font-size:16px;color:var(--blue);line-height:20px}
.cap-text{width:142px;font-size:6px;line-height:8.6px;color:#555}
.cap-text p+p{margin-top:8px}
/* about */
.bio{left:53px;top:266px;width:175px;font-size:7px;line-height:10.3px;color:#222;text-align:justify}
.bio p+p{margin-top:10px}
.clients-band{left:0;top:580px;width:431px;height:259px;background:var(--tint)}
.client{width:61px;height:67px;background:var(--white);box-shadow:0 1px 3px rgba(0,0,0,.08);display:flex;align-items:center;justify-content:center;text-align:center;font-weight:700;font-size:7px;color:#4a4a4a;padding:0 4px;line-height:9px}
/* contact */
.info-item{display:flex;align-items:center;gap:6px;font-size:7px;line-height:9px;color:#222}
.info-item .ico{width:16px;height:16px;border-radius:50%;background:var(--blue);display:flex;align-items:center;justify-content:center}
.contact-card{left:54px;top:363px;width:323px;height:196px;background:var(--white);box-shadow:0 1px 8px rgba(0,0,0,.1)}
.field{border:1px solid var(--blue);border-radius:9px;height:17px;font-size:5.5px;color:var(--label);padding:5px 9px;background:var(--white)}
.field.message{border-radius:11px;height:71px}
.map{left:0;top:600px;width:431px;height:147px;background:linear-gradient(160deg,#ece5d6 0%,#f6f1e6 22%,#e3dccd 40%,#f3eee4 58%,#e8dfcf 74%,#eef0e4 88%,#dfe9d8 100%)}
</style>
</head>
<body>

<div class="page-label" style="left:329px;top:50px">Our Work</div>
<div class="page-label" style="left:830px;top:50px">Capabilities</div>
<div class="page-label" style="left:341px;top:1367px">About Us</div>
<div class="page-label" style="left:811px;top:1432px">Contact</div>

<!-- Our Work page -->
<section class="panel" style="left:126px;top:111px;height:1209px">
  <header class="site-header">
    <div class="wordmark">LARKFIELD PROSE STUDIO</div>
    <nav class="site-nav"><a>HOME</a><a class="active">OUR WORK</a><a>CAPABILITIES</a><a>ABOUT US</a><a>CONTACT</a></nav>
    <div class="btn-touch">GET IN TOUCH</div>
  </header>
  <div class="hero"><div class="hero-photo" role="img" aria-label="Photo of a businessman in a suit writing at a desk beside a laptop"></div><h1 class="hero-title">Larkfield<br>Prose<br>Studio</h1></div>
  <h2 class="section-title" style="top:221px">Our Work</h2>
  <p class="section-intro" style="top:255px;width:268px">Lorem ipsum dolor sit amet, consectetur adipiscing elit, sed do eiusmod tempor incididunt ut labore et dolore magna aliquam suspendisse ultrices gravid commodo viverra maecenas accumsan lacus vel facilisis.</p>
  <div style="left:54px;top:305px;width:101px;height:125px;background:linear-gradient(160deg,#6f757c 0%,#b9bdc2 30%,#ecebea 55%,#f7f5f4 75%,#d9d6d5 100%)" role="img" aria-label="Writing sample: laptop with printed pages and a red pen"></div>
  <div style="left:165px;top:305px;width:212px;height:125px;background:linear-gradient(115deg,#2a2c30 0%,#4a4d52 25%,#cfd0d2 45%,#f2f2f1 62%,#c5c6c8 80%,#1d1f22 100%)" role="img" aria-label="Writing sample: hand signing a document"></div>
  <div style="left:54px;top:441px;width:101px;height:125px;background:linear-gradient(150deg,#dfe6ee 0%,#7f98b6 30%,#c7d1dc 55%,#f1f3f5 80%,#9aa7b6 100%)" role="img" aria-label="Writing sample: hands reviewing a report"></div>
  <div style="left:165px;top:441px;width:101px;height:125px;background:linear-gradient(140deg,#c9c8c7 0%,#f4f3f2 35%,#efe6e4 60%,#f7f5f4 80%,#d8d4d2 100%)" role="img" aria-label="Writing sample: edited page with red pen marks"></div>
  <div style="left:276px;top:441px;width:101px;height:125px;background:linear-gradient(90deg,#e8e8e6 0%,#d4d3d0 40%,#8a8c8f 60%,#4b4e52 80%,#2f3236 100%)" role="img" aria-label="Writing sample: presenter at a whiteboard"></div>
  <div style="left:54px;top:578px;width:212px;height:125px;background:linear-gradient(120deg,#f6e2c0 0%,#c79b6c 30%,#9a7556 50%,#c9b99a 70%,#8d8a6a 100%)" role="img" aria-label="Writing sample: hand writing with a pen in warm light"></div>
  <div style="left:276px;top:578px;width:101px;height:125px;background:linear-gradient(150deg,#c9d3de 0%,#7d8fa5 35%,#a6b4c4 60%,#5c6d82 100%)" role="img" aria-label="Writing sample: business meeting"></div>
  <div class="btn-pill" style="left:184px;top:721px;width:63px;height:20px;line-height:20px">LOAD MORE</div>
  <div class="divider" style="top:776px"></div>
  <h2 class="section-title" style="top:800px">Testimonials</h2>
  <div class="testimonial" style="left:45px;top:846px"><span class="quote-mark">“</span><p>Lorem ipsum dolor sit met on losectetur adipis loing elit, dolor eiusmod tempor incidi dunt ut labore et dol oreagna alliolquam uspe ndi sse ltri lorerces gravid comm lore jsodde oiverra maecenas accumloresan lacus vel facilisis.</p><div class="avatar" role="img" aria-label="Client portrait"></div><div class="name">Aaron Vale</div><div class="stars">★★★★★</div></div>
  <div class="testimonial" style="left:162px;top:846px"><span class="quote-mark">“</span><p>Lorem ipsum dolor sit met on losectetur adipis loing elit, dolor eiusmod tempor incidi dunt ut labore et dol oreagna alliolquam uspe ndi sse ltri lorerces gravid comm lore jsodde oiverra maecenas accumloresan lacus vel facilisis.</p><div class="avatar" role="img" aria-label="Client portrait"></div><div class="name">Aaron Vale</div><div class="stars">★★★★★</div></div>
  <div class="testimonial" style="left:279px;top:846px"><span class="quote-mark">“</span><p>Lorem ipsum dolor sit met on losectetur adipis loing elit, dolor eiusmod tempor incidi dunt ut labore et dol oreagna alliolquam uspe ndi sse ltri lorerces gravid comm lore jsodde oiverra maecenas accumloresan lacus vel facilisis.</p><div class="avatar" role="img" aria-label="Client portrait"></div><div class="name">Aaron Vale</div><div class="stars">★★★★★</div></div>
  <div class="dots" style="top:1028px">••••••</div>
  <footer class="site-footer" style="top:1072px;height:137px">Footer Section</footer>
</section>

<!-- Capabilities page -->
<section class="panel" style="left:613px;top:111px;height:1270px">
  <header class="site-header">
    <div class="wordmark">LARKFIELD PROSE STUDIO</div>
    <nav class="site-nav"><a>HOME</a><a>OUR WORK</a><a class="active">CAPABILITIES</a><a>ABOUT US</a><a>CONTACT</a></nav>
    <div class="btn-touch">GET IN TOUCH</div>
  </header>
  <div class="hero"><div class="hero-photo" role="img" aria-label="Photo of a businessman in a suit writing at a desk beside a laptop"></div><h1 class="hero-title">Larkfield<br>Prose<br>Studio</h1></div>
  <h2 class="section-title" style="top:221px">Capabilities</h2>
  <p class="section-intro" style="top:255px;width:268px">Lorem ipsum dolor sit amet, consectetur adipiscing elit, sed do eiusmod tempor incididunt ut labore et dolore magna aliquam suspendisse ultrices gravid commodo viverra maecenas accumsan lacus vel facilisis.</p>

  <div class="cap-image skew-left" style="left:54px;top:319px;background:linear-gradient(125deg,#1d3a66 0%,#5d86bd 25%,#c9dcf0 45%,#7b9cc6 62%,#2c4672 80%,#a9bfdc 100%)" role="img" aria-label="Chess pieces over a digital city network"></div>
  <div class="cap-icon" style="left:177px;top:375px"><svg width="24" height="24" viewBox="0 0 24 24" fill="none" stroke="#1f62a8" stroke-width="1.4"><rect x="4" y="3" width="16" height="13" rx="1"/><path d="M7 7h6M7 10h4"/><circle cx="15" cy="17" r="3.5"/><path d="M15 12.5v1M15 20.5v1M10.5 17h1M18.5 17h1"/></svg></div>
  <h3 class="cap-title" style="left:236px;top:333px">STRATEGY</h3>
  <div class="cap-text" style="left:236px;top:364px"><p>Lorem ipsum dolor sit amet, consectetur radip iscing elit, sed do eiusmod tempor inc idiodunt ut labore et dolore magna aliqua. Quis ipshuye umj suspendisse ultrices grafvida. Risus lorem com modo viverra maecenas accumsan lacus vel facilisi orem ipsum dolor sit amet.</p><p>Lorem ipsum dolor sit amet, consectetur radip iscing elit, sed do eiusmod tempor inc idiodunt ut labore et dolore magna aliqua. Quis ipshuye umj suspendisse ultrices grafvida. Risus lorem com modo viverra maecenas accumsa</p></div>

  <h3 class="cap-title" style="left:54px;top:533px">COACHING</h3>
  <div class="cap-text" style="left:54px;top:564px"><p>Lorem ipsum dolor sit amet, consectetur radip iscing elit, sed do eiusmod tempor inc idiodunt ut labore et dolore magna aliqua. Quis ipshuye umj suspendisse ultrices grafvida. Risus lorem com modo viverra maecenas accumsan lacus vel facilisi orem ipsum dolor sit amet.</p><p>Lorem ipsum dolor sit amet, consectetur radip iscing elit, sed do eiusmod tempor inc idiodunt ut labore et dolore magna aliqua. Quis ipshuye umj suspendisse ultrices grafvida. Risus lorem com modo viverra maecenas accumsa</p></div>
  <div class="cap-image skew-right" style="left:231px;top:518px;background:linear-gradient(100deg,#f1efec 0%,#c8c2ba 25%,#3a2f29 42%,#b79f86 58%,#8e7a68 72%,#d9d3cc 88%,#4e4a46 100%)" role="img" aria-label="Coach speaking to a seated group"></div>
  <div class="cap-icon" style="left:210px;top:573px"><svg width="24" height="24" viewBox="0 0 24 24" fill="none" stroke="#1f62a8" stroke-width="1.4"><rect x="8" y="3" width="13" height="9" rx="1"/><circle cx="5" cy="7" r="2"/><path d="M3 15v-4h4v4M5 15v5"/><circle cx="10" cy="17" r="1.5"/><circle cx="15" cy="17" r="1.5"/><circle cx="20" cy="17" r="1.5"/><path d="M8 21h14"/></svg></div>

  <div class="cap-image skew-left" style="left:54px;top:719px;background:linear-gradient(150deg,#cfc7bb 0%,#efebe5 30%,#b8a895 48%,#f3f0ec 65%,#e6e2dc 100%)" role="img" aria-label="Hand writing with a pen on white paper"></div>
  <div class="cap-icon" style="left:171px;top:776px"><svg width="24" height="24" viewBox="0 0 24 24" fill="none" stroke="#1f62a8" stroke-width="1.4"><rect x="4" y="3" width="13" height="18" rx="1"/><path d="M7 7h7M7 10h7M7 13h4"/><path d="M20 10l-7 8-2 1 1-2 7-8z"/></svg></div>
  <h3 class="cap-title" style="left:236px;top:732px">WRITING</h3>
  <div class="cap-text" style="left:236px;top:763px"><p>Lorem ipsum dolor sit amet, consectetur radip iscing elit, sed do eiusmod tempor inc idiodunt ut labore et dolore magna aliqua. Quis ipshuye umj suspendisse ultrices grafvida. Risus lorem com modo viverra maecenas accumsan lacus vel facilisi orem ipsum dolor sit amet.</p><p>Lorem ipsum dolor sit amet, consectetur radip iscing elit, sed do eiusmod tempor inc idiodunt ut labore et dolore magna aliqua. Quis ipshuye umj suspendisse ultrices grafvida. Risus lorem com modo viverra maecenas accumsa</p></div>

  <h3 class="cap-title" style="left:54px;top:932px">EDITING</h3>
  <div class="cap-text" style="left:54px;top:963px"><p>Lorem ipsum dolor sit amet, consectetur radip iscing elit, sed do eiusmod tempor inc idiodunt ut labore et dolore magna aliqua. Quis ipshuye umj suspendisse ultrices grafvida. Risus lorem com modo viverra maecenas accumsan lacus vel facilisi orem ipsum dolor sit amet.</p><p>Lorem ipsum dolor sit amet, consectetur radip iscing elit, sed do eiusmod tempor inc idiodunt ut labore et dolore magna aliqua. Quis ipshuye umj suspendisse ultrices grafvida. Risus lorem com modo viverra maecenas accumsa</p></div>
  <div class="cap-image skew-right" style="left:231px;top:917px;background:linear-gradient(165deg,#b9a37f 0%,#e4d6bd 28%,#f1e4da 45%,#f6f4f2 62%,#e9d9cf 80%,#c7b9ad 100%)" role="img" aria-label="Hand marking up a printed page with a red pencil"></div>
  <div class="cap-icon" style="left:209px;top:971px"><svg width="24" height="24" viewBox="0 0 24 24" fill="none" stroke="#1f62a8" stroke-width="1.4"><rect x="3" y="3" width="18" height="18" rx="2"/><path d="M3 7h18"/><path d="M16 10l-7 7-2 .5.5-2 7-7z"/></svg></div>
  <footer class="site-footer" style="top:1131px;height:139px">Footer Section</footer>
</section>

<!-- About Us page -->
<section class="panel" style="left:126px;top:1421px;height:976px">
  <header class="site-header">
    <div class="wordmark">LARKFIELD PROSE STUDIO</div>
    <nav class="site-nav"><a>HOME</a><a>OUR WORK</a><a>CAPABILITIES</a><a class="active">ABOUT US</a><a>CONTACT</a></nav>
    <div class="btn-touch">GET IN TOUCH</div>
  </header>
  <div class="hero"><div class="hero-photo" role="img" aria-label="Photo of a businessman in a suit writing at a desk beside a laptop"></div><h1 class="hero-title">Larkfield<br>Prose<br>Studio</h1></div>
  <h2 class="section-title" style="top:220px">About Us</h2>
  <div class="bio">
    <p>Daniel Hartwell has provided freelance marketing writing and editing services since 1999. He first began working in the IT industry in 1992 with a systems integration company where he managed a service department that eventually grew to a staff of 150. During this time, Daniel interacted with senior-level technology experts and developed the ability to translate technical terms and concepts into language that communicates business value.</p>
    <p>Daniel transitioned into corporate communications in 1997, taking advantage of his degree in journalism from Brookmere University. Since that time and during his freelance career, he has helped hundreds of companies convey corporate messaging and product-value statements through written documents such as customer success stories, white papers, ghost-written articles, press releases, newsletter articles and website text.</p>
    <p>Daniel's technology writing experience includes virtualization, cloud computing, enterprise applications, mobility, IT security, application development and testing, business intelligence, systems integration, content management and storage.</p>
  </div>
  <div style="left:255px;top:266px;width:123px;height:133px;background:linear-gradient(90deg,#c9c3b8 0%,#b8a898 35%,#d9b9a2 55%,#c7c9d4 80%,#aeb4c4 100%)" role="img" aria-label="Portrait of the studio founder"></div>
  <div style="left:255px;top:409px;width:123px;height:124px;background:linear-gradient(140deg,#1f5f96 0%,#4a8fc4 30%,#a9cde6 55%,#eef2f5 78%,#c9ced3 100%)" role="img" aria-label="Hand writing in a spiral notebook"></div>
  <div class="clients-band"></div>
  <h2 class="section-title" style="top:613px">Our Clients</h2>
  <div class="client" style="left:22px;top:662px">Northgate Media</div>
  <div class="client" style="left:87px;top:662px">Pellworth</div>
  <div class="client" style="left:153px;top:662px">Lumicor</div>
  <div class="client" style="left:218px;top:662px">Brightfold</div>
  <div class="client" style="left:284px;top:662px">Tasklane</div>
  <div class="client" style="left:349px;top:662px">Quillbase</div>
  <div class="client" style="left:54px;top:742px">Orvane</div>
  <div class="client" style="left:120px;top:742px">Netharbor</div>
  <div class="client" style="left:185px;top:742px">Stonevault</div>
  <div class="client" style="left:251px;top:742px">Kestrel</div>
  <div class="client" style="left:316px;top:742px">Veloxa</div>
  <footer class="site-footer" style="top:839px;height:137px">Footer Section</footer>
</section>

<!-- Contact page -->
<section class="panel" style="left:613px;top:1483px;height:875px">
  <header class="site-header">
    <div class="wordmark">LARKFIELD PROSE STUDIO</div>
    <nav class="site-nav"><a>HOME</a><a>OUR WORK</a><a>CAPABILITIES</a><a>ABOUT US</a><a class="active">CONTACT</a></nav>
    <div class="btn-touch">GET IN TOUCH</div>
  </header>
  <div class="hero"><div class="hero-photo" role="img" aria-label="Photo of a businessman in a suit writing at a desk beside a laptop"></div><h1 class="hero-title">Larkfield<br>Prose<br>Studio</h1></div>
  <h2 class="section-title" style="top:220px">Contact Us</h2>
  <p class="section-intro" style="top:255px;width:235px">Lorem ipsum dolor sit amet, consectetur adipiscing elit, sed do eiusmod tempor incididunt ut labore et dolore magna aliqua. Ut enim ad minim veniam, quis nostrud exercitation ullamco labo.</p>
  <div class="info-item" style="left:82px;top:313px"><span class="ico"><svg width="8" height="8" viewBox="0 0 24 24" fill="#fff"><path d="M6.6 10.8a15 15 0 006.6 6.6l2.2-2.2a1 1 0 011-.25 11.4 11.4 0 003.6.57 1 1 0 011 1V20a1 1 0 01-1 1A17 17 0 013 4a1 1 0 011-1h3.5a1 1 0 011 1 11.4 11.4 0 00.57 3.6 1 1 0 01-.25 1z"/></svg></span><span>Phone<br>+00 4410 5532</span></div>
  <div class="info-item" style="left:173px;top:313px"><span class="ico"><svg width="8" height="8" viewBox="0 0 24 24" fill="#fff"><path d="M3 5h18v14H3z"/><path d="M3 5l9 7 9-7" stroke="#1f62a8" stroke-width="2" fill="none"/></svg></span><span>Email<br>hello@lpstudio.net</span></div>
  <div class="info-item" style="left:273px;top:313px"><span class="ico"><svg width="8" height="8" viewBox="0 0 24 24" fill="#fff"><path d="M12 2a7 7 0 00-7 7c0 5 7 13 7 13s7-8 7-13a7 7 0 00-7-7zm0 9.5A2.5 2.5 0 1112 6.5a2.5 2.5 0 010 5z"/></svg></span><span>Orchard Lane 14<br>3100 Westbury</span></div>
  <div class="contact-card"></div>
  <div class="field" style="left:78px;top:394px;width:135px">Name:</div>
  <div class="field" style="left:219px;top:394px;width:135px">Email:</div>
  <div class="field" style="left:78px;top:420px;width:135px">Phone:</div>
  <div class="field" style="left:219px;top:420px;width:135px">Subject:</div>
  <div class="field message" style="left:78px;top:448px;width:276px">Message</div>
  <div class="btn-pill" style="left:181px;top:511px;width:70px;height:19px;line-height:19px;font-size:7px">SUBMIT</div>
  <div class="map" role="img" aria-label="Street map showing the studio location"></div>
  <footer class="site-footer" style="top:747px;height:128px">Footer Section</footer>
</section>

</body>
</html>
```